Cybersecurity company is looking for business card.

I need a business card design for our company, we are a cybersecurity company providing advance technology to protect agains any kind of malware. We need a fresh modern design it should communicate modern, technology and growth.

Target Market(s)

Business to business

Industry/Entity Type

Business

Contact Information for Business Card

Should have location, address, fax, mobile, phone, email and website.

Requirements
Must have
• Must follow company's logo color and style. Must have the company's log on its.

```html
<!DOCTYPE html>
<html lang="en">
<head>
<meta charset="utf-8">
<title>Vextrel Business Card</title>
<link rel="stylesheet" href="https://fonts.googleapis.com/css2?family=Open+Sans:wght@400;600;700;800&display=swap">
<style>
  :root {
    --backdrop: #4a3222;
    --card: #f7f7f5;
    --ink: #111111;
    --brand-red: #a31f24;
    --text-grey: #555555;
    --white: #ffffff;
  }
  * { margin: 0; padding: 0; box-sizing: border-box; }
  html, body { width: 1200px; height: 480px; overflow: hidden; }
  body {
    background: var(--backdrop);
    font-family: "Open Sans", Arial, sans-serif;
    position: relative;
  }
  .card {
    position: absolute;
    width: 474px;
    height: 268px;
    background: var(--card);
    box-shadow: 0 2px 6px rgba(0,0,0,0.35);
  }
  .card--front { left: 109px; top: 97px; }
  .card--back { left: 637px; top: 97px; }

  .wordmark {
    position: absolute;
    left: 0; right: 0;
    text-align: center;
    font-weight: 800;
    color: var(--ink);
    letter-spacing: 1px;
    line-height: 1;
  }
  .card--front .wordmark { top: 52px; font-size: 60px; }
  .card--back .wordmark { top: 102px; font-size: 60px; }

  .band { position: absolute; left: 0; top: 155px; width: 474px; height: 26px; }
  .band__name {
    position: absolute; left: 34px; top: 159px;
    color: var(--white); font-size: 16px; font-weight: 600; line-height: 18px;
  }
  .band__name small { font-size: 12.5px; font-weight: 400; margin-left: 3px; }
  .band__web {
    position: absolute; left: 334px; top: 161px;
    color: var(--white); font-size: 12px; font-weight: 700; line-height: 16px;
  }

  .contact {
    position: absolute; left: 0; right: 0; top: 199px;
    text-align: center; color: var(--text-grey); font-size: 11.5px; line-height: 17px;
  }
  .contact .city { color: var(--brand-red); font-weight: 700; font-size: 13.5px; }
  .contact .label { color: var(--brand-red); font-weight: 700; }
  .contact .gap { margin-left: 8px; }
</style>
</head>
<body>
  <div class="card card--front">
    <div class="wordmark">vextrel</div>
    <svg class="band" viewBox="0 0 474 26" aria-hidden="true">
      <path d="M0 0 H292 Q296 0 293 5 L286 20 Q283 26 276 26 H0 Z" fill="var(--ink)"/>
      <path d="M474 0 H308 Q300 0 297 6 L289 22 Q287 26 292 26 H474 Z" fill="var(--brand-red)"/>
    </svg>
    <div class="band__name">Your Name Here,<small>Designation</small></div>
    <div class="band__web">www.vextrel.com</div>
    <div class="contact">
      <p>Harbor Tech Park (HTP) - Meridian Avenue Road, <span class="city">Lisbon - PT</span></p>
      <p><span class="label">M:</span> +351 91 234 XXXX <span class="label gap">T:</span> 21 234 XXXX <span class="label gap">F:</span> 21 234 XXXX</p>
      <p><span class="label">E:</span> name.surname@vextrel.com</p>
    </div>
  </div>

  <div class="card card--back">
    <div class="wordmark">vextrel</div>
  </div>
</body>
</html>
```